Business Cards for accounting firm

Need a file and design that we can update for our employees when we get a design we like. Logo is attached.
Megan Tolliver CPA
Owner
P.O. Box 918
Kestrel Falls ND 58990
4195550148
megan@brindlecrestltd.com
www.brindlecrestltd.com
Industry/Entity Type
Accounting

```html
<!DOCTYPE html>
<html lang="en">
<head>
<meta charset="utf-8">
<title>Brindlecrest Dental CPA's Ltd – Business Card</title>
<link rel="stylesheet" href="https://fonts.googleapis.com/css2?family=Open+Sans:wght@400;600;700&display=swap">
<style>
  :root {
    --page: #e9e9e7;
    --card-front: #ffffff;
    --card-back: #6a6a6b;
    --brand-blue: #2aa4de;
    --ink: #5a5a5c;
    --rule: #cfcfd1;
    --white: #ffffff;
  }
  * { margin: 0; padding: 0; box-sizing: border-box; }
  html, body {
    width: 1200px; height: 948px; overflow: hidden;
    background: var(--page);
    font-family: "Open Sans", Arial, sans-serif;
  }
  .sheet {
    width: 1200px; height: 948px;
    display: flex; flex-direction: column; align-items: center; justify-content: center;
    gap: 64px;
  }
  .card {
    width: 640px; height: 366px;
    position: relative;
    box-shadow: 0 6px 18px rgba(0,0,0,.14);
  }
  .card--front { background: var(--card-front); }
  .card--back {
    background: var(--card-back);
    display: flex; flex-direction: column; align-items: center; justify-content: center;
  }

  .brand-name { font-weight: 700; line-height: 1.05; text-align: center; }
  .card--front .brand-name {
    position: absolute; top: 52px; left: 0; right: 0;
    font-size: 40px; color: var(--brand-blue);
  }
  .card--back .brand-name { font-size: 44px; color: var(--white); }
  .brand-name span { display: block; }
  .brand-name .brand-sub { font-size: .45em; margin-top: 4px; }

  .contact {
    position: absolute; left: 56px; right: 56px; top: 212px;
    display: flex; align-items: stretch;
  }
  .contact__person {
    flex: 1; text-align: right; padding-right: 24px;
    font-size: 15px; color: var(--ink); line-height: 1.55;
  }
  .contact__name { color: var(--brand-blue); font-weight: 700; font-size: 17px; }
  .contact__role { margin-bottom: 8px; }
  .contact__divider { width: 1px; background: var(--rule); }
  .contact__lines {
    flex: 1; padding-left: 24px; list-style: none;
    font-size: 15px; color: var(--ink); line-height: 1.9;
  }
  .contact__lines li { display: flex; align-items: center; gap: 10px; white-space: nowrap; }
  .contact__icon { width: 16px; height: 16px; flex: none; }

  .back-web { margin-top: 26px; color: var(--white); font-size: 16px; letter-spacing: 2px; }
</style>
</head>
<body>
<main class="sheet">

  <section class="card card--front" aria-label="Business card front">
    <h1 class="brand-name"><span>Brindlecrest Dental</span><span class="brand-sub">CPA's Ltd</span></h1>

    <div class="contact">
      <div class="contact__person">
        <p class="contact__name">Megan Tolliver CPA</p>
        <p class="contact__role">Owner</p>
        <p>P.O. Box 918</p>
        <p>Kestrel Falls ND 58990</p>
      </div>
      <div class="contact__divider"></div>
      <ul class="contact__lines">
        <li>
          <svg class="contact__icon" viewBox="0 0 16 16" aria-hidden="true"><circle cx="8" cy="8" r="8" fill="var(--brand-blue)"/><path d="M5.4 4.2l1.5 1.6-.8 1.1c.5 1.2 1.4 2.1 2.6 2.6l1.1-.8 1.6 1.5-.8 1.3C8.2 11.4 4.6 7.8 4.1 5z" fill="#fff"/></svg>
          <span>555-555-0148</span>
        </li>
        <li>
          <svg class="contact__icon" viewBox="0 0 16 16" aria-hidden="true"><circle cx="8" cy="8" r="8" fill="var(--brand-blue)"/><rect x="4" y="5" width="8" height="6" rx="1" fill="#fff"/><path d="M4.3 5.4L8 8.3l3.7-2.9" stroke="var(--brand-blue)" stroke-width="1" fill="none"/></svg>
          <span>megan@brindlecrestltd.com</span>
        </li>
        <li>
          <svg class="contact__icon" viewBox="0 0 16 16" aria-hidden="true"><circle cx="8" cy="8" r="8" fill="var(--brand-blue)"/><circle cx="8" cy="8" r="4" fill="none" stroke="#fff" stroke-width="1.1"/><path d="M4 8h8M8 4c-1.6 2.4-1.6 5.6 0 8M8 4c1.6 2.4 1.6 5.6 0 8" stroke="#fff" stroke-width="1" fill="none"/></svg>
          <span>www.brindlecrestltd.com</span>
        </li>
      </ul>
    </div>
  </section>

  <section class="card card--back" aria-label="Business card back">
    <h2 class="brand-name"><span>Brindlecrest Dental</span><span class="brand-sub">CPA's Ltd</span></h2>
    <p class="back-web">www.brindlecrestltd.com</p>
  </section>

</main>
</body>
</html>
```